Texas Recycling and dump company needs Flyer design

We need a flyer design for a new company based in Austin Texas called 'Salvage Grove'. We receive dump materials on our property along with sell repurposed materials. We would like our design to include our logo along with add some creative designs to the flyer. Please use the attached image file as an outline. Blank boxes can be used for additional images.

Target Market(s)

Handing out flyers to new companies and hopefully getting contracts with them.

Font styles to use
Serif
Sans Serif

Requirements
Must have
• double sided
• images
Nice to have
• QR code with our website

```html
<!DOCTYPE html>
<html lang="en">
<head>
<meta charset="utf-8">
<title>Salvage Grove Flyer – Front and Back</title>
<link href="https://fonts.googleapis.com/css2?family=Montserrat:wght@400;600;700&family=Oswald:wght@400;500&family=Libre+Baskerville&display=swap" rel="stylesheet">
<style>
  :root {
    --backdrop: #e4e4e4;
    --paper: #ffffff;
    --panel-grey: #f2f2f2;
    --brand-green: #7dc142;
    --brand-blue: #1f6fb8;
    --ink: #1e1e1e;
    --ink-soft: #555555;
    --rule-gold: #f0d35a;
    --bar-grey: #ececec;
  }
  * { box-sizing: border-box; margin: 0; padding: 0; }
  html, body { width: 1200px; height: 1200px; overflow: hidden; }
  body { background: var(--backdrop); position: relative; font-family: "Montserrat", sans-serif; color: var(--ink); }

  .flyer {
    position: absolute; top: 237px;
    width: 560px; height: 725px;
    background: var(--paper);
    box-shadow: 0 4px 18px rgba(0,0,0,.16);
    overflow: hidden;
  }
  .flyer.front { left: 25px; }
  .flyer.back { left: 615px; }

  .grey-panel { position: absolute; left: 315px; right: 0; bottom: 0; background: var(--panel-grey); }
  .front .grey-panel { top: 320px; }
  .back .grey-panel { top: 140px; }

  /* header */
  .brand { position: absolute; left: 40px; top: 46px; display: flex; align-items: center; gap: 8px; }
  .brand-mark { width: 22px; height: 22px; background: var(--brand-green); }
  .brand-name { font-weight: 600; font-size: 19px; color: var(--brand-blue); letter-spacing: .3px; }
  .tagline-bar { position: absolute; left: 230px; top: 22px; width: 290px; height: 26px; background: var(--bar-grey);
    font-size: 9.5px; letter-spacing: 2.4px; line-height: 26px; padding-left: 14px; color: var(--ink-soft); white-space: nowrap; }
  .tagline-bar b { color: var(--ink); font-weight: 700; }
  .tagline-block { position: absolute; left: 520px; top: 22px; width: 40px; height: 18px; background: var(--brand-blue); }
  .header-url { position: absolute; left: 244px; top: 56px; font-size: 8px; color: var(--ink); }

  /* front hero */
  .hero-photo { position: absolute; left: 0; top: 95px; width: 315px; height: 225px;
    background: radial-gradient(circle at 45% 55%, #8bc34a 0%, #4e7d2a 45%, #263f14 100%); }
  .hero-panel { position: absolute; left: 315px; top: 95px; width: 245px; height: 225px; background: var(--brand-green);
    padding: 34px 0 0 30px; color: #fff; }
  .hero-words { font-family: "Libre Baskerville", serif; font-size: 30px; line-height: 1.25; }
  .hero-rule { width: 180px; height: 1px; background: #fff; margin: 12px 0 9px; }
  .hero-sub { font-family: "Oswald", sans-serif; font-size: 13px; letter-spacing: 1px; }

  .rule { position: absolute; height: 1px; background: var(--rule-gold); }

  .section-label { position: absolute; font-weight: 700; font-size: 10px; letter-spacing: .8px; color: var(--ink); }

  /* material figures */
  .material { position: absolute; }
  .material .photo { width: 100%; }
  .material figcaption { text-align: right; font-weight: 700; font-size: 9.5px; letter-spacing: .8px; margin-top: 6px; }
  .asphalt { left: 200px; top: 372px; width: 140px; }
  .asphalt .photo { height: 86px; background: linear-gradient(135deg, #4a4a4d, #2f2f31); }
  .clean-fill { left: 385px; top: 335px; width: 135px; }
  .clean-fill .photo { height: 80px; background: linear-gradient(180deg, #d6c3a0, #b3925e); }
  .concrete { left: 40px; top: 392px; width: 140px; }
  .concrete .photo { height: 84px; background: linear-gradient(135deg, #b9bcc0, #6d7176); }
  .cd { left: 365px; top: 462px; width: 150px; }
  .cd .photo { height: 84px; background: linear-gradient(160deg, #a88a6a, #6b4c33); }
  .wood { left: 190px; top: 500px; width: 150px; }
  .wood .photo { height: 82px; background: linear-gradient(135deg, #d9ae72, #9d6c34); }

  .motto { position: absolute; left: 40px; top: 610px; font-family: "Oswald", sans-serif; font-size: 22px; color: var(--brand-blue); letter-spacing: .5px; white-space: nowrap; }

  .phone-bar { position: absolute; left: 62px; top: 655px; width: 245px; height: 40px; background: var(--brand-green);
    font-family: "Oswald", sans-serif; font-size: 25px; color: #fff; line-height: 40px; padding-left: 44px; letter-spacing: 1.5px; }
  .phone-badge { position: absolute; left: 30px; top: 646px; width: 58px; height: 58px; border-radius: 50%;
    background: #6f6f6f; border: 5px solid var(--brand-blue); box-shadow: inset 0 0 0 3px #fff; }
  .phone-badge svg { position: absolute; left: 13px; top: 13px; }

  .location { position: absolute; display: flex; gap: 10px; align-items: center; }
  .front .location { left: 335px; top: 652px; }
  .address { font-size: 10px; line-height: 1.35; color: var(--ink-soft); white-space: nowrap; }
  .address strong { font-weight: 700; }

  .footer-url { position: absolute; right: 40px; top: 701px; font-weight: 700; font-size: 11px; letter-spacing: .8px; color: var(--ink); }

  /* back */
  .deals-head { position: absolute; left: 40px; right: 0; top: 100px; display: flex; align-items: center; gap: 10px; }
  .deals-title { font-family: "Oswald", sans-serif; font-size: 24px; color: var(--brand-blue); letter-spacing: .5px; }
  .deals-bar { flex: 1; height: 18px; background: var(--brand-green); }
  .mulch { left: 340px; top: 160px; width: 180px; }
  .mulch .photo { height: 110px; background: linear-gradient(160deg, #6f8f4a, #3b4f2a 60%, #2a2a2a); }
  .garden-a { left: 340px; top: 310px; width: 180px; }
  .garden-a .photo { height: 110px; background: linear-gradient(160deg, #a59a84, #5f7a45 60%, #8a6f58); }
  .garden-b { left: 340px; top: 460px; width: 180px; }
  .garden-b .photo { height: 110px; background: linear-gradient(160deg, #b0a58e, #6a8450 55%, #8d725a); }
  .earth-line { position: absolute; left: 40px; top: 600px; font-family: "Oswald", sans-serif; font-size: 22px; color: var(--brand-blue); letter-spacing: .5px; }
  .back .location { left: 340px; top: 640px; }
</style>
</head>
<body>
  <article class="flyer front">
    <div class="grey-panel"></div>
    <header>
      <div class="brand"><span class="brand-mark"></span><span class="brand-name">SALVAGE GROVE</span></div>
      <div class="tagline-bar">GIVE YOUR GARBAGE <b>ANOTHER LIFE</b></div>
      <div class="tagline-block"></div>
      <div class="header-url">www.salvagegrove.com</div>
    </header>

    <section class="hero">
      <div class="hero-photo" role="img" aria-label="A hand holding a green glass globe topped with leaves, against a blurred green background"></div>
      <div class="hero-panel">
        <div class="hero-words">REDUCE<br>REUSE<br>RECYCLE</div>
        <div class="hero-rule"></div>
        <div class="hero-sub">FOR A BETTER TOMORROW</div>
      </div>
    </section>

    <div class="rule" style="left:40px; top:340px; width:330px;"></div>

    <section class="materials">
      <div class="section-label" style="left:40px; top:372px;">OVERVIEW</div>
      <figure class="material asphalt"><div class="photo" role="img" aria-label="Close-up of crushed asphalt"></div><figcaption>ASPHALT</figcaption></figure>
      <figure class="material clean-fill"><div class="photo" role="img" aria-label="A mound of clean fill dirt"></div><figcaption>CLEAN FILL</figcaption></figure>
      <figure class="material concrete"><div class="photo" role="img" aria-label="A pile of broken concrete blocks"></div><figcaption>CONCRETE</figcaption></figure>
      <figure class="material cd"><div class="photo" role="img" aria-label="A heap of construction and demolition debris"></div><figcaption>C&amp;D</figcaption></figure>
      <figure class="material wood"><div class="photo" role="img" aria-label="A pile of wood scraps and brush"></div><figcaption>WOOD/ BRUSH</figcaption></figure>
    </section>

    <div class="motto">CLEANER THE PRODUCT, LOWER THE PRICE</div>
    <div class="rule" style="left:335px; top:644px; width:185px;"></div>

    <div class="phone-bar">512 555 0148</div>
    <div class="phone-badge">
      <svg width="22" height="22" viewBox="0 0 24 24" aria-hidden="true">
        <path fill="#111" d="M6.6 10.8a15.1 15.1 0 0 0 6.6 6.6l2.2-2.2a1 1 0 0 1 1-.25 11.4 11.4 0 0 0 3.6.57 1 1 0 0 1 1 1V20a1 1 0 0 1-1 1A17 17 0 0 1 3 4a1 1 0 0 1 1-1h3.5a1 1 0 0 1 1 1c0 1.25.2 2.45.57 3.57a1 1 0 0 1-.25 1z"/>
      </svg>
    </div>

    <div class="location">
      <svg width="24" height="34" viewBox="0 0 24 34" aria-hidden="true">
        <path fill="#111" d="M12 0C5.4 0 0 5.2 0 11.7 0 20.5 12 34 12 34s12-13.5 12-22.3C24 5.2 18.6 0 12 0zm0 16.5a4.8 4.8 0 1 1 0-9.6 4.8 4.8 0 0 1 0 9.6z"/>
      </svg>
      <div class="address"><strong>SALVAGE GROVE</strong><br>2180, CEDAR HOLLOW RD<br>AUSTIN, TEXAS</div>
    </div>

    <div class="rule" style="left:40px; top:718px; width:480px;"></div>
    <div class="footer-url">www.salvagegrove.com</div>
  </article>

  <article class="flyer back">
    <div class="grey-panel"></div>
    <header>
      <div class="brand"><span class="brand-mark"></span><span class="brand-name">SALVAGE GROVE</span></div>
      <div class="tagline-bar">GIVE YOUR GARBAGE <b>ANOTHER LIFE</b></div>
      <div class="tagline-block"></div>
      <div class="header-url">www.salvagegrove.com</div>
    </header>

    <div class="deals-head"><span class="deals-title">BEST DEALS</span><span class="deals-bar"></span></div>

    <section class="products">
      <figure class="material mulch"><div class="photo" role="img" aria-label="Landscaped front yard bed covered in dark mulch"></div><figcaption>MULCH</figcaption></figure>
      <figure class="material garden-a"><div class="photo" role="img" aria-label="Stone path through a flowering garden"></div><figcaption>ABCDEF</figcaption></figure>
      <figure class="material garden-b"><div class="photo" role="img" aria-label="Stone path through a flowering garden"></div><figcaption>ABCDEF</figcaption></figure>
    </section>

    <div class="earth-line">GIVE A GOOD LIFE TO EARTH</div>

    <div class="location">
      <svg width="24" height="34" viewBox="0 0 24 34" aria-hidden="true">
        <path fill="#111" d="M12 0C5.4 0 0 5.2 0 11.7 0 20.5 12 34 12 34s12-13.5 12-22.3C24 5.2 18.6 0 12 0zm0 16.5a4.8 4.8 0 1 1 0-9.6 4.8 4.8 0 0 1 0 9.6z"/>
      </svg>
      <div class="address"><strong>SALVAGE GROVE</strong><br>2180, CEDAR HOLLOW RD<br>AUSTIN, TEXAS</div>
    </div>

    <div class="rule" style="left:40px; top:700px; width:480px;"></div>
  </article>
</body>
</html>
```